Bright Harbour Fitness

BRIGHT HARBOUR FITNESS PTY LTD, We are a revolutionary, fresh, new entity to the fitness industry looking to make a mark within and support local communities where we are situated. My business partner and i come with a broad range of skill sets and possess the ability and motivation to ensure our philosophy works - and the philosophy is simple - to help people improve their everyday life and well-being. Be it, helping them with their health and fitness, changing their appearance, improving motivation, setting and achieving goals or by helping them become part of a positive team atmosphere.
Our stores visual appearance, like our training concepts, is quite different to the normal run of the mill gym. It's fresh, it's vibrant, it looks great, and we know it will be a real head turner guaranteed to attract attention. This is definitely the future of fitness.
We would like to see on one side our Info and on the other side our LOGO, colour scheme is in the LOGO.
Final design should tell people "We Help People Look And Feel Bright As The Harbour!

Industry/Entity Type

Training

Contact Information for Business Card

Corwin
0412 386 054
cor@brightharbourfitness.com.au
217 Kestrelvale Rd Wattlebrook NSW 2188

Requirements
Must have
• Our Logo

```html
<!DOCTYPE html>
<html lang="en">
<head>
<meta charset="utf-8">
<title>Bright Harbour Fitness – Business Card</title>
<link href="https://fonts.googleapis.com/css2?family=Lato:wght@700;900&display=swap" rel="stylesheet">
<style>
  :root {
    --backdrop: #5a2c16;
    --orange: #f7993a;
    --orange-band: #f19a3e;
    --white: #ffffff;
    --ink: #474747;
    --ink-dark: #333333;
  }
  html, body {
    margin: 0;
    padding: 0;
    width: 1200px;
    height: 957px;
    overflow: hidden;
    background: var(--backdrop);
    font-family: "Lato", Arial, sans-serif;
  }
  .canvas {
    position: relative;
    width: 1200px;
    height: 957px;
  }
  .card {
    position: absolute;
    border-radius: 22px;
    overflow: hidden;
  }
  .tab {
    position: absolute;
    height: 12px;
    background: var(--white);
  }
  .tab--top { top: 0; border-radius: 0 0 6px 6px; }
  .tab--bottom { bottom: 0; border-radius: 6px 6px 0 0; }

  /* Front */
  .card--front {
    left: 289px; top: 93px;
    width: 583px; height: 335px;
    background: var(--orange);
  }
  .card--front .tab { left: 92px; width: 400px; }
  .brand-line {
    position: absolute;
    left: 82px; top: 136px;
    display: flex; align-items: center; gap: 20px;
  }
  .brand-mark {
    width: 58px; height: 58px;
    background: var(--ink);
    border-radius: 6px;
  }
  .brand-name {
    font-weight: 900;
    font-size: 20px;
    letter-spacing: 1.6px;
    color: var(--ink);
    white-space: nowrap;
  }

  /* Back */
  .card--back {
    left: 280px; top: 521px;
    width: 601px; height: 346px;
    background: var(--orange-band);
  }
  .card--back .tab { left: 95px; width: 412px; }
  .info-band {
    position: absolute;
    left: 0; top: 62px;
    width: 100%; height: 222px;
    background: var(--white);
  }
  .brand-stack {
    position: absolute;
    left: 60px; top: 74px;
    display: flex; align-items: center; gap: 14px;
  }
  .brand-stack .brand-mark { width: 78px; height: 78px; }
  .brand-stack .brand-name {
    font-size: 17px;
    line-height: 19px;
    letter-spacing: 0.4px;
    margin-top: 18px;
  }
  .divider {
    position: absolute;
    left: 277px; top: 67px;
    width: 2px; height: 118px;
    background: var(--orange);
  }
  .contact {
    position: absolute;
    left: 295px; top: 80px;
    color: var(--ink-dark);
  }
  .contact__name {
    margin: 0 0 11px 8px;
    font-size: 28px;
    font-weight: 700;
    color: var(--ink);
    line-height: 1;
  }
  .contact__line {
    margin: 0 0 5px 0;
    font-size: 10px;
    font-weight: 700;
    line-height: 11px;
    white-space: nowrap;
  }
  .contact__line--phone { margin-left: 2px; font-size: 9px; }
  .contact__line--email { font-size: 11px; }
</style>
</head>
<body>
<main class="canvas">
  <section class="card card--front" aria-label="Card front">
    <span class="tab tab--top"></span>
    <div class="brand-line">
      <span class="brand-mark"></span>
      <span class="brand-name">BRIGHT HARBOUR FITNESS</span>
    </div>
    <span class="tab tab--bottom"></span>
  </section>

  <section class="card card--back" aria-label="Card back">
    <span class="tab tab--top"></span>
    <div class="info-band">
      <div class="brand-stack">
        <span class="brand-mark"></span>
        <span class="brand-name">BRIGHT<br>HARBOUR<br>FITNESS</span>
      </div>
      <span class="divider"></span>
      <div class="contact">
        <p class="contact__name">Corwin</p>
        <p class="contact__line contact__line--phone">Phone : 0412 386 054</p>
        <p class="contact__line">Adress :217 Kestrelvale Rd Wattlebrook NSW 2188</p>
        <p class="contact__line contact__line--email">Email : cor@brightharbourfitness.com.au</p>
      </div>
    </div>
    <span class="tab tab--bottom"></span>
  </section>
</main>
</body>
</html>
```